Billboard For Marcus Delvane

Need a Billboard 8ft. High x 16ft. Long. Ive attached a former billboard and looking for the same thing just updated with:
Wardens Guild Award Logo - 2020, 2022
Summit Lantern award Logo - 2022

Thanks.

```html
<!DOCTYPE html>
<html lang="en">
<head>
<meta charset="utf-8">
<title>Billboard – Marcus Delvane</title>
<link rel="stylesheet" href="https://fonts.googleapis.com/css2?family=Oswald:wght@300;400&family=Poppins:ital,wght@0,400;0,500;0,600;0,700;0,800;1,800&display=swap">
<style>
  :root {
    --red: #ee0a12;
    --red-deep: #c90008;
    --black: #0e0e0e;
    --charcoal: #2a2a2a;
    --white: #ffffff;
    --backdrop: #cdcdcd;
    --portrait-top: #b9b4ae;
    --portrait-bottom: #3a55a4;
  }
  * { margin: 0; padding: 0; box-sizing: border-box; }
  html, body {
    width: 915px; height: 1200px; overflow: hidden;
    background: var(--backdrop);
  }
  .billboard {
    position: absolute;
    left: 30px; top: 386px;
    width: 855px; height: 428px;
    box-shadow: 0 6px 18px rgba(0,0,0,.28);
  }
  .billboard svg { display: block; width: 100%; height: 100%; }
  .headline { font-family: "Poppins", sans-serif; font-weight: 800; font-style: italic; }
  .name { font-family: "Poppins", sans-serif; font-weight: 700; }
  .title { font-family: "Poppins", sans-serif; font-weight: 600; }
  .phone { font-family: "Poppins", sans-serif; font-weight: 700; }
  .tagline { font-family: "Poppins", sans-serif; font-weight: 700; letter-spacing: 2px; }
  .brand { font-family: "Poppins", sans-serif; font-weight: 700; }
  .award-small { font-family: "Poppins", sans-serif; font-weight: 500; }
  .award { font-family: "Oswald", sans-serif; font-weight: 300; }
</style>
</head>
<body>
  <div class="billboard">
    <svg viewBox="0 0 1304 652" xmlns="http://www.w3.org/2000/svg">
      <defs>
        <linearGradient id="portraitFill" x1="0" y1="0" x2="0" y2="1">
          <stop offset="0" stop-color="var(--portrait-top)"/>
          <stop offset="0.55" stop-color="#d9a88e"/>
          <stop offset="0.62" stop-color="var(--portrait-bottom)"/>
          <stop offset="1" stop-color="#2f4b97"/>
        </linearGradient>
        <linearGradient id="headerFill" x1="0" y1="0" x2="1" y2="1">
          <stop offset="0" stop-color="var(--black)"/>
          <stop offset="1" stop-color="var(--charcoal)"/>
        </linearGradient>
        <linearGradient id="phoneBand" x1="0" y1="0" x2="1" y2="0">
          <stop offset="0" stop-color="var(--red-deep)"/>
          <stop offset="1" stop-color="var(--red)"/>
        </linearGradient>
      </defs>

      <!-- base -->
      <rect class="panel-base" width="1304" height="652" fill="var(--white)"/>

      <!-- corner blocks and header -->
      <polygon class="corner-left" points="0,0 208,0 345,262 0,262" fill="var(--red)"/>
      <polygon class="header-band" points="240,0 1205,0 1304,170 1304,262 372,262" fill="url(#headerFill)"/>
      <polygon class="corner-right" points="1236,0 1304,0 1304,122" fill="var(--red)"/>

      <!-- info bands -->
      <polygon class="phone-band" points="285,345 1304,345 1304,462 340,462" fill="url(#phoneBand)"/>
      <rect class="tagline-band" x="430" y="462" width="874" height="54" fill="var(--black)"/>

      <!-- portrait area -->
      <path class="portrait" role="img" aria-label="Portrait photo of Marcus Delvane, smiling, in a blue shirt and tie"
            d="M40,652 L40,560 C40,500 80,470 130,440 C90,400 60,340 60,260 C60,140 140,58 230,58 C320,58 340,150 340,260 C340,340 310,400 300,430 C380,450 440,480 470,530 L512,652 Z"
            fill="url(#portraitFill)"/>

      <!-- headline -->
      <text class="headline" x="392" y="130" font-size="116" fill="var(--white)" textLength="452" lengthAdjust="spacingAndGlyphs">BUYING</text>
      <circle class="or-badge" cx="917" cy="86" r="42" fill="var(--red)"/>
      <text class="headline" x="917" y="101" font-size="40" fill="var(--white)" text-anchor="middle">OR</text>
      <text class="headline" x="387" y="230" font-size="118" fill="var(--white)" textLength="525" lengthAdjust="spacingAndGlyphs">SELLING?</text>
      <text class="headline" x="945" y="230" font-size="118" fill="var(--red)" textLength="282" lengthAdjust="spacingAndGlyphs">CALL</text>

      <!-- name -->
      <text class="name" x="442" y="326" font-size="64" textLength="576" lengthAdjust="spacingAndGlyphs">
        <tspan fill="var(--black)">MARCUS </tspan><tspan fill="var(--red)">DELVANE</tspan>
      </text>
      <text class="title" x="1034" y="300" font-size="24" fill="var(--black)">SALES</text>
      <text class="title" x="1034" y="326" font-size="24" fill="var(--black)">REPRESENTATIVE</text>

      <!-- phone -->
      <circle class="phone-icon" cx="478" cy="403" r="44" fill="var(--black)"/>
      <path d="M462,381 l10,-4 l8,16 l-7,5 c3,8 8,14 15,18 l6,-6 l15,9 l-4,10 c-4,5 -12,5 -20,1 c-14,-8 -25,-21 -30,-36 c-2,-6 -1,-10 7,-13 z"
            fill="var(--red)"/>
      <path d="M492,378 a22,22 0 0 1 18,18 M490,388 a12,12 0 0 1 10,10" stroke="var(--red)" stroke-width="4" fill="none" stroke-linecap="round"/>
      <text class="phone" x="543" y="440" font-size="106" fill="var(--white)" textLength="710" lengthAdjust="spacingAndGlyphs">613.555.0142</text>

      <!-- tagline -->
      <text class="tagline" x="450" y="503" font-size="37" textLength="808" lengthAdjust="spacingAndGlyphs">
        <tspan fill="var(--white)">FOCUSED, DRIVEN, AND </tspan><tspan fill="var(--red)">EXPERIENCED!</tspan>
      </text>

      <!-- brokerage name -->
      <rect class="brand-mark" x="510" y="552" width="26" height="26" fill="var(--red)"/>
      <text class="brand" x="544" y="576" font-size="25" fill="var(--black)">HARBOR CREST</text>

      <!-- award: summit lantern -->
      <circle class="award-badge" cx="775" cy="578" r="22" fill="var(--black)"/>
      <text class="award-small" x="803" y="549" font-size="10" fill="var(--black)">HARBOR CREST</text>
      <text class="award" x="802" y="572" font-size="22" fill="var(--black)">SUMMIT LANTERN</text>
      <text class="award" x="802" y="596" font-size="22" fill="var(--black)">AWARD 2022</text>

      <!-- award: wardens guild -->
      <circle class="award-badge" cx="1001" cy="578" r="30" fill="none" stroke="var(--black)" stroke-width="2"/>
      <circle cx="1001" cy="578" r="20" fill="var(--black)"/>
      <text class="award-small" x="1038" y="553" font-size="9" fill="var(--black)">HARBOR CREST</text>
      <text class="award" x="1038" y="573" font-size="19" font-weight="400" fill="var(--black)">WARDENS GUILD</text>
      <text class="award" x="1038" y="593" font-size="16" font-weight="400" fill="var(--black)">AWARD 2020, 2022</text>
      <text class="award-small" x="1038" y="607" font-size="8" fill="var(--black)">NATIONAL TOP 1%</text>

      <!-- social handle -->
      <circle class="social-dot" cx="1180" cy="580" r="8" fill="var(--red)"/>
      <text class="brand" x="1194" y="586" font-size="15" fill="var(--red)">@mdelvane</text>
    </svg>
  </div>
</body>
</html>
```